Spiritual journeyer, astrologer, Reiki master, underground music lover needs business card design

Initially I need a business card design (and possibly a logo for my new website). I offer astrological and energetic inquiry and guidance to clients in support of their life's evolutionary path. I combine an eclectic mix of methods with a focus on the mind body connection. I am a spiritual journeyer, astrologer, Reiki Master, certified personal trainer, soon to be black belt in Taekwondo (karate), and researcher into the benefits of music/sound vibrational therapy. And underground music lover :) The attached drawing is just something I drew freehand, it is symbolic of many things important to me. I wanted the figure to clearly be female. Her arms are open to catch the sky, the name of my new business is Orlabrook, and Orla is my daughter's name. This was just an idea I had, I'm open to suggestions. The photo is me with the planets in the sky as they were at the moment I was born (some years ago-LOL)
Updates

I have picked a final design. Thank you everyone for your time and effort.

Target Market(s)

Worldwide, what I do can be done in person or anywhere in the world via Skype

Industry/Entity Type

Professional Service

Contact Information for Business Card

Simple, unusual image with my business name and contact info

Font styles to use
Sans Serif

Requirements
Must have
• My website very clean, simple. Somehow combine biz name of Orlabrook with female figure catching/holding the starry sky? See my poor drawing I attached.
Nice to have
• Something that conveys all the unique, unusual, eclectic skills and capacities I have
Should not have
• Frilly, fancy, stuffy

```html
<!DOCTYPE html>
<html lang="en">
<head>
<meta charset="utf-8">
<title>Orlabrook Business Card</title>
<link rel="stylesheet" href="https://fonts.googleapis.com/css2?family=Open+Sans:wght@400;600;700&display=swap">
<style>
  :root {
    --bg: #e9e6e1;
    --card: #ffffff;
    --ink: #1e1e1e;
    --grey: #5a5a5a;
    --orange: #ee7d1c;
    --rule: #d4d4d4;
    --photo-red: #b8322c;
    --photo-wood: #a8744a;
    --photo-cream: #e9e0d2;
  }
  * { box-sizing: border-box; margin: 0; padding: 0; }
  html, body {
    width: 1200px; height: 950px; overflow: hidden;
    background: var(--bg);
    font-family: "Open Sans", Arial, sans-serif;
  }
  .card {
    position: absolute;
    width: 700px; height: 400px;
    background: var(--card);
    box-shadow: 0 8px 24px rgba(0,0,0,0.18);
    overflow: hidden;
  }
  /* Photo side */
  .card--photo { left: 130px; top: 50px; }
  .card__photo {
    position: absolute; inset: 0;
    background:
      linear-gradient(180deg, rgba(0,0,0,0) 55%, rgba(120,80,50,0.35) 100%),
      linear-gradient(100deg, var(--photo-red) 0%, #c7453a 35%, var(--photo-cream) 55%, var(--photo-wood) 100%);
  }
  .card__photo-brand {
    position: absolute; right: 50px; top: 150px;
    display: flex; flex-direction: column; align-items: center; gap: 10px;
  }
  .brand-mark {
    width: 90px; height: 90px; border-radius: 50%;
    border: 3px solid var(--ink);
  }
  .brand-name {
    font-weight: 700; font-size: 34px; color: var(--ink);
    letter-spacing: 0.5px; text-transform: uppercase;
  }
  /* Contact side */
  .card--info { left: 370px; top: 500px; }
  .card__brand {
    position: absolute; left: 50px; top: 80px; width: 270px;
    display: flex; flex-direction: column; align-items: center; gap: 14px;
  }
  .card__brand .brand-mark { width: 130px; height: 130px; }
  .card__divider {
    position: absolute; left: 350px; top: 40px; bottom: 40px;
    width: 1px; background: var(--rule);
  }
  .card__details { position: absolute; left: 380px; top: 48px; right: 24px; }
  .person-name { font-size: 22px; font-weight: 600; color: var(--ink); margin-bottom: 10px; }
  .roles { list-style: none; color: var(--orange); font-size: 17px; line-height: 1.3; margin-bottom: 18px; }
  .tagline { color: var(--grey); font-size: 16px; line-height: 1.35; margin-bottom: 12px; }
  .contacts { list-style: none; color: var(--grey); font-size: 16px; line-height: 1.55; }
  .contacts li { display: flex; align-items: center; gap: 8px; }
  .contacts svg { width: 15px; height: 15px; fill: var(--orange); flex: none; }
</style>
</head>
<body>
  <section class="card card--photo">
    <div class="card__photo" role="img" aria-label="Photo of the practitioner seated on the floor of a red-walled treatment room beside a massage table"></div>
    <div class="card__photo-brand">
      <span class="brand-mark"></span>
      <span class="brand-name">Orlabrook</span>
    </div>
  </section>

  <section class="card card--info">
    <div class="card__brand">
      <span class="brand-mark"></span>
      <span class="brand-name">Orlabrook</span>
    </div>
    <div class="card__divider"></div>
    <div class="card__details">
      <h1 class="person-name">Maren Holt</h1>
      <ul class="roles">
        <li>Spiritual journeyer</li>
        <li>Astrologer, Reiki Master</li>
        <li>Certified personal trainer</li>
      </ul>
      <p class="tagline">Astrological and Energetic<br>Guidance and Inquery</p>
      <ul class="contacts">
        <li><svg viewBox="0 0 16 16"><path d="M3.5 1.5l2.5 0 1 3.5-1.6 1.2c.8 1.7 2.2 3.1 3.9 3.9L10.5 8.5l3.5 1v2.5c0 1-1 2-2 2C6.5 14 2 9.5 2 4c0-1 .5-2.5 1.5-2.5z"/></svg>555-014-2736</li>
        <li><svg viewBox="0 0 16 16"><path d="M1 3h14v10H1z M1.8 3.8L8 8.8l6.2-5" stroke="#fff" stroke-width="1.2"/></svg>email@orlabrook.com</li>
        <li><svg viewBox="0 0 16 16"><path d="M8 1a5 5 0 0 0-5 5c0 4 5 9 5 9s5-5 5-9a5 5 0 0 0-5-5zm0 7a2 2 0 1 1 0-4 2 2 0 0 1 0 4z"/></svg>www.orlabrook.com</li>
      </ul>
    </div>
  </section>
</body>
</html>
```